Business Card for Medical Laboratory Data Processor
logo design just finished
Use same font as used in my logo
Marcel Ondrak, MBA, CNE, MCSE
Chief Technology Officer
47 Fenwick Ave
Millbrook, OH 44812
marcel.ondrak@threlgo.com
www.threlgo.com
we would like business card to use same look/logo as the attached new logo. Using the same font is good, but optional.
We are interested in including a QR code on either front or back of the card.
AI Files for new logo. (from just finished contest)

```html
<!DOCTYPE html>
<html lang="en">
<head>
<meta charset="utf-8">
<title>Threlgo Business Card</title>
<link href="https://fonts.googleapis.com/css2?family=Exo+2:wght@400;600;700&display=swap" rel="stylesheet">
<style>
  :root {
    --page-bg: #e6e7e9;
    --card-white: #ffffff;
    --brand-blue: #1b6fae;
    --brand-blue-deep: #0b4a80;
    --brand-blue-light: #3f9bd6;
    --brand-green: #3e9a3c;
    --ink: #1f3d5c;
    --ink-soft: #5b6f84;
    --contact-text: #e8f3fb;
  }
  * { box-sizing: border-box; margin: 0; padding: 0; }
  html, body { width: 1200px; height: 987px; overflow: hidden; }
  body {
    background: var(--page-bg);
    font-family: "Exo 2", Arial, sans-serif;
    position: relative;
  }
  .card {
    position: absolute;
    width: 640px;
    height: 366px;
    border-radius: 22px;
    background: var(--card-white);
    overflow: hidden;
    box-shadow: 0 10px 28px rgba(0, 0, 0, 0.18);
  }
  .card-back { left: 110px; top: 70px; }
  .card-front { left: 450px; top: 540px; }

  .back-brand {
    position: absolute;
    left: 0; right: 0; top: 118px;
    display: flex; align-items: center; justify-content: center; gap: 14px;
  }
  .brand-dot {
    width: 22px; height: 22px; border-radius: 50%;
    background: var(--brand-green);
  }
  .brand-name {
    font-weight: 700;
    color: var(--brand-blue);
    letter-spacing: 3px;
  }
  .back-brand .brand-name { font-size: 52px; }
  .back-web {
    position: absolute; left: 0; right: 0; top: 218px;
    text-align: center;
    font-size: 15px; letter-spacing: 6px;
    color: var(--ink);
  }

  .front-waves { position: absolute; inset: 0; }
  .front-brand {
    position: absolute; left: 34px; top: 30px;
    display: flex; align-items: center; gap: 10px;
  }
  .front-brand .brand-dot { width: 16px; height: 16px; }
  .front-brand .brand-name { font-size: 36px; }
  .person {
    position: absolute; left: 36px; top: 98px;
  }
  .person-name { font-size: 14px; font-weight: 600; color: var(--ink); }
  .person-title { font-size: 12px; color: var(--ink-soft); margin-top: 2px; }

  .contact-list {
    position: absolute; right: 34px; bottom: 30px;
    list-style: none;
    color: var(--contact-text);
    font-size: 12.5px;
    line-height: 1.55;
  }
  .contact-list li { display: flex; align-items: center; gap: 8px; }
  .contact-list li.indent { padding-left: 22px; }
  .contact-icon { width: 14px; height: 14px; flex: none; }
</style>
</head>
<body>

<section class="card card-back" aria-label="Card back">
  <div class="back-brand">
    <span class="brand-dot"></span>
    <span class="brand-name">THRELGO</span>
  </div>
  <p class="back-web">www.threlgo.com</p>
</section>

<section class="card card-front" aria-label="Card front">
  <svg class="front-waves" viewBox="0 0 640 366" preserveAspectRatio="none" aria-hidden="true">
    <defs>
      <radialGradient id="blueField" cx="0.55" cy="0.55" r="0.7">
        <stop offset="0" stop-color="#3f9bd6"/>
        <stop offset="0.6" stop-color="#1b6fae"/>
        <stop offset="1" stop-color="#0b4a80"/>
      </radialGradient>
    </defs>
    <path d="M0,168 C190,128 400,140 640,58 L640,92 C420,160 200,150 0,196 Z" fill="#3e9a3c"/>
    <path d="M0,206 C210,160 420,176 640,108 L640,126 C420,194 210,182 0,222 Z" fill="#1b6fae"/>
    <path d="M0,236 C220,188 430,204 640,138 L640,366 L0,366 Z" fill="url(#blueField)"/>
  </svg>

  <div class="front-brand">
    <span class="brand-dot"></span>
    <span class="brand-name">THRELGO</span>
  </div>

  <div class="person">
    <p class="person-name">Marcel Ondrak, MBA, CNE, MCSE</p>
    <p class="person-title">Chief Technology Officer</p>
  </div>

  <ul class="contact-list">
    <li>
      <svg class="contact-icon" viewBox="0 0 14 14" aria-hidden="true"><path d="M7 1a4 4 0 0 1 4 4c0 3-4 8-4 8S3 8 3 5a4 4 0 0 1 4-4z" fill="#fff"/><circle cx="7" cy="5" r="1.5" fill="#1b6fae"/></svg>
      47 Fenwick Ave
    </li>
    <li class="indent">Millbrook, OH 44812</li>
    <li>
      <svg class="contact-icon" viewBox="0 0 14 14" aria-hidden="true"><path d="M3 1h2l1 3-1.5 1a7 7 0 0 0 4.5 4.5L10 8l3 1v2c0 1-1 2-2 2A10 10 0 0 1 1 3c0-1 1-2 2-2z" fill="#fff"/></svg>
      T 734.555.0142
    </li>
    <li>
      <svg class="contact-icon" viewBox="0 0 14 14" aria-hidden="true"><rect x="2" y="5" width="10" height="6" rx="1" fill="#fff"/><rect x="4" y="2" width="6" height="3" fill="#fff"/></svg>
      F 734.555.0187
    </li>
    <li>
      <svg class="contact-icon" viewBox="0 0 14 14" aria-hidden="true"><rect x="1" y="3" width="12" height="8" rx="1" fill="#fff"/><path d="M1.5 3.5 7 8l5.5-4.5" stroke="#1b6fae" fill="none"/></svg>
      marcel.ondrak@threlgo.com
    </li>
    <li>
      <svg class="contact-icon" viewBox="0 0 14 14" aria-hidden="true"><circle cx="7" cy="7" r="5.5" stroke="#fff" fill="none"/><path d="M1.5 7h11M7 1.5c2.5 3 2.5 8 0 11M7 1.5c-2.5 3-2.5 8 0 11" stroke="#fff" fill="none"/></svg>
      www.threlgo.com
    </li>
  </ul>
</section>

</body>
</html>
```